Product Introduction Brochure

Brochure to introduce our mid/high end lighting products to potential wholesalers / Disrtibutors / Retailers. To be mainly graphical but will contain some text also. The purpose of the brochure will be to get potential customers to find out more either by calling us or to visit our website. The brochure should be of A3 size folded in half to an A4. Front page should be mainly logo and name, inner 2 pages should showcase some of the products we can supply together with some text (to be supplied, please use filler text in the initial design), then the back page containing our contact details. The products are lights, floor lamps and table lamps. I have attached a number of images, as well as our company logo. I would prefer the design to be on a black background, however this is not critical
Target Market(s)
Retailer, distribution and wholesale buyers
Interior design consultants and specifiers
Industry/Entity Type
Product
Look and feel
Each slider illustrates characteristics of the customer's brand and the style your logo design should communicate.

```html
<!DOCTYPE html>
<html lang="en">
<head>
<meta charset="utf-8">
<title>Lumora – Product Brochure Cover</title>
<link rel="stylesheet" href="https://fonts.googleapis.com/css2?family=Poppins:wght@600&display=swap">
<style>
  :root {
    --page-black: #000000;
    --brand-green: #2ba53f;
    --deco-sage: #8a9a7e;
    --deco-mid: #5a8660;
    --deco-deep: #04412a;
  }
  html, body {
    margin: 0;
    padding: 0;
    width: 860px;
    height: 1200px;
    overflow: hidden;
    background: var(--page-black);
  }
  .cover {
    position: relative;
    width: 860px;
    height: 1200px;
    background: var(--page-black);
    overflow: hidden;
  }
  .cover-art {
    position: absolute;
    left: 0;
    display: block;
  }
  .cover-art--top { top: 0; }
  .cover-art--bottom { bottom: 0; }
  .brand-lockup {
    position: absolute;
    left: 0;
    right: 0;
    top: 380px;
    height: 150px;
    display: flex;
    align-items: center;
    justify-content: center;
    gap: 30px;
  }
  .brand-dot {
    width: 150px;
    height: 150px;
    border-radius: 50%;
    background: var(--brand-green);
    flex: none;
  }
  .brand-name {
    margin: 0;
    font-family: "Poppins", sans-serif;
    font-weight: 600;
    font-size: 112px;
    line-height: 1;
    letter-spacing: -2px;
    color: var(--brand-green);
  }
</style>
</head>
<body>
  <main class="cover">
    <svg class="cover-art cover-art--top" width="860" height="300" viewBox="0 0 860 300"
         role="img" aria-label="Soft green geometric decoration in sage and deep green tones">
      <defs>
        <linearGradient id="top-fade" x1="0" y1="0" x2="0" y2="1">
          <stop offset="0" stop-color="#4a6b4c"/>
          <stop offset="1" stop-color="#000000"/>
        </linearGradient>
      </defs>
      <rect x="140" y="0" width="600" height="300" fill="url(#top-fade)"/>
    </svg>

    <section class="brand-lockup">
      <span class="brand-dot" aria-hidden="true"></span>
      <h1 class="brand-name">Lumora</h1>
    </section>

    <svg class="cover-art cover-art--bottom" width="860" height="480" viewBox="0 0 860 480"
         role="img" aria-label="Soft green geometric decoration in sage, mid green and deep green tones">
      <defs>
        <linearGradient id="bottom-fade" x1="0" y1="0" x2="1" y2="1">
          <stop offset="0" stop-color="#000000"/>
          <stop offset="0.35" stop-color="#6f8a64"/>
          <stop offset="0.7" stop-color="#2f7a3a"/>
          <stop offset="1" stop-color="#04412a"/>
        </linearGradient>
      </defs>
      <rect x="140" y="0" width="600" height="480" fill="url(#bottom-fade)"/>
    </svg>
  </main>
</body>
</html>
```